Postcard Flyer For Plumbing Company

We are a p[professional plumbing company in NSW that carry out plumbing, electrical and hot water system work.
i want to send a postcard size flyer 105mm x 148mm to our clients to offer $xx off their next job they book with us.
The front of the flyer needs to say.... Feel The Love WIth $35 Off your Next Job. It needs to include a section where their name and postal address can go (74mm W x 24mm H) on the left hand side of the bottom of the flyer - refer attached example.
The other side of the flyer needs to have a section for text, the offer ($35 or $xx what they get off their next job) and also can use the tag line... Call 1 Number for The Best In 3 Trades - Plumbing, Hot Water & Electrical.
Plumbing, hot water and electrical pictures/icons can be used.
I want the flyer to stand out, use the corporate colours and be modern whilst letting them know that they can use this voucher on their next job.
Refer attachments.

Target Market(s)

Homeowners and our existing clients

Industry/Entity Type

Plumbing

Font styles to use
Serif

Colors
0255a3
ec1f27
ffffff
d3d3d3

Requirements
Must have
• Corporate colours and logos
• Red Colour:
• C=0
• M=100
• Y=100
• K=0
• Blue Colour
• C= 100
• M=66
• Y=0
• K=2
• Grey Colour
• C= 26
• M=21
• Y=19
• K=0
Nice to have
• predominately white background
Should not have
• Black background and lots of black.

```html
<!DOCTYPE html>
<html lang="en">
<head>
<meta charset="utf-8">
<title>Harlow Contracting – Postcard Flyer</title>
<link href="https://fonts.googleapis.com/css2?family=Oswald:wght@500;600&family=Roboto:wght@400;500;700;900&display=swap" rel="stylesheet">
<style>
  :root{
    --blue:#0255a3;
    --red:#ec1f27;
    --white:#ffffff;
    --grey:#d3d3d3;
    --stage:#b5b5b5;
    --ink:#222;
    --yellow:#ffe600;
  }
  *{box-sizing:border-box;margin:0;padding:0}
  html,body{width:1200px;height:1200px;overflow:hidden}
  body{background:var(--stage);font-family:"Roboto",Arial,sans-serif;position:relative}
  .card{position:absolute;left:205px;width:759px;background:var(--white);overflow:hidden;box-shadow:6px 6px 10px rgba(0,0,0,.45)}
  .card--front{top:34px;height:538px}
  .card--back{top:628px;height:539px}
  .card__art{position:absolute;inset:0;width:100%;height:100%}
  .abs{position:absolute;white-space:nowrap}

  /* brand */
  .brand{font-family:"Roboto",Arial,sans-serif;font-weight:700;color:var(--blue);line-height:1}
  .brand--front{left:42px;top:46px;font-size:46px;width:310px}
  .brand--back{left:455px;top:34px;font-size:26px;width:200px;text-align:center}
  .trades{font-weight:700;color:var(--ink);letter-spacing:-.2px}
  .trades--front{left:41px;top:155px;font-size:19px}
  .trades--back{left:455px;top:103px;font-size:11.5px;width:200px;text-align:center}

  /* address block */
  .address{left:29px;top:360px;width:381px;height:123px;padding:12px 18px 0 18px;font-size:11px;font-weight:700;color:var(--ink)}
  .address__row{display:flex;align-items:flex-end;height:21px}
  .address__row span{margin-right:5px}
  .address__row i{flex:1;border-bottom:2px dotted #444;height:1px;margin-bottom:3px}
  .address__row--gap{margin-top:4px}

  /* offers */
  .offer{text-align:center}
  .offer--front{left:492px;top:345px;width:200px;color:var(--white)}
  .offer__amount{font-family:"Oswald","Arial Narrow",sans-serif;font-weight:600;line-height:1}
  .offer--front .offer__amount{color:var(--yellow);font-size:78px}
  .offer__off{font-size:.4em;margin-left:4px}
  .offer__line{font-weight:700;font-size:16.5px;line-height:1.45;margin-top:6px}
  .offer--back{left:25px;top:360px;width:200px}
  .offer--back .offer__amount{color:var(--blue);font-size:72px}
  .offer--back .offer__off{color:var(--red)}

  /* footer */
  .url{left:0;width:759px;top:500px;text-align:center;color:var(--white);font-size:17px;letter-spacing:2.6px}
  .card--back .url{top:502px;padding-left:120px}

  /* back content */
  .headline{left:346px;width:410px;text-align:center}
  .headline__top{top:148px;font-family:"Oswald","Arial Narrow",sans-serif;font-weight:500;font-size:40px;color:#3a3a3a;line-height:1.1;transform:scaleX(.85);transform-origin:center}
  .headline__sub{top:196px;font-weight:700;font-size:32px;color:var(--blue);line-height:1.1}
  .service{width:120px;text-align:center;top:313px;font-size:20px;color:var(--ink)}
  .emergency{left:228px;top:392px;width:507px;height:43px;display:flex;align-items:center;padding-left:30px;color:var(--white)}
  .emergency__ask{font-weight:700;font-size:14px;margin-right:10px}
  .emergency__num{font-weight:900;font-size:33px;letter-spacing:.5px}
  .contact{top:450px;font-weight:700;font-size:19px;color:var(--ink)}
</style>
</head>
<body>

<svg width="0" height="0" style="position:absolute" aria-hidden="true">
  <defs>
    <symbol id="burst" viewBox="-100 -100 200 200">
      <polygon points="100,0 87.2,11.5 96.6,25.9 81.3,33.7 86.6,50 69.8,53.6 70.7,70.7 53.6,69.8 50,86.6 33.7,81.3 25.9,96.6 11.5,87.2 0,100 -11.5,87.2 -25.9,96.6 -33.7,81.3 -50,86.6 -53.6,69.8 -70.7,70.7 -69.8,53.6 -86.6,50 -81.3,33.7 -96.6,25.9 -87.2,11.5 -100,0 -87.2,-11.5 -96.6,-25.9 -81.3,-33.7 -86.6,-50 -69.8,-53.6 -70.7,-70.7 -53.6,-69.8 -50,-86.6 -33.7,-81.3 -25.9,-96.6 -11.5,-87.2 0,-100 11.5,-87.2 25.9,-96.6 33.7,-81.3 50,-86.6 53.6,-69.8 70.7,-70.7 69.8,-53.6 86.6,-50 81.3,-33.7 96.6,-25.9 87.2,-11.5"/>
    </symbol>
    <linearGradient id="workshop" x1="0" y1="0" x2="1" y2="1">
      <stop offset="0" stop-color="#c3d0de"/>
      <stop offset=".5" stop-color="#e6ebf0"/>
      <stop offset="1" stop-color="#cfd8e2"/>
    </linearGradient>
    <radialGradient id="glow" cx=".45" cy=".45" r=".65">
      <stop offset="0" stop-color="#3c5ee0"/>
      <stop offset=".55" stop-color="#15299a"/>
      <stop offset="1" stop-color="#050c3f"/>
    </radialGradient>
    <filter id="soft" x="-20%" y="-20%" width="140%" height="140%">
      <feDropShadow dx="2" dy="3" stdDeviation="3" flood-opacity=".35"/>
    </filter>
  </defs>
</svg>

<!-- FRONT -->
<section class="card card--front">
  <svg class="card__art" viewBox="0 0 759 538">
    <path role="img" aria-label="Photo: plumber servicing a hot water system" d="M290,0 C350,110 375,240 380,355 C520,355 650,372 759,405 L759,0 Z" fill="url(#workshop)"/>
    <path d="M282,0 C344,112 368,242 372,362" fill="none" stroke="var(--red)" stroke-width="9"/>
    <path d="M268,0 C332,116 356,246 360,372" fill="none" stroke="var(--blue)" stroke-width="5"/>
    <path d="M372,362 C520,360 650,378 759,412" fill="none" stroke="var(--red)" stroke-width="9"/>
    <path d="M360,373 C520,372 655,395 759,440" fill="none" stroke="var(--blue)" stroke-width="5"/>
    <path d="M560,485 C640,470 710,460 759,420 L759,485 Z" fill="var(--white)"/>
    <path d="M600,485 C680,470 730,455 759,440" fill="none" stroke="var(--red)" stroke-width="8"/>
    <path d="M640,485 C700,478 740,470 759,462" fill="none" stroke="var(--blue)" stroke-width="6"/>

    <g filter="url(#soft)">
      <circle role="img" aria-label="Photo: white drain pipe fitting" cx="88" cy="267" r="56" fill="var(--blue)" stroke="var(--white)" stroke-width="3"/>
      <circle role="img" aria-label="Photo: light bulb" cx="213" cy="267" r="56" fill="var(--red)" stroke="var(--white)" stroke-width="3"/>
      <circle role="img" aria-label="Photo: chrome hot water tap handle" cx="340" cy="272" r="56" fill="#c8c8c8" stroke="var(--white)" stroke-width="3"/>
    </g>

    <rect x="29" y="360" width="381" height="123" fill="var(--white)" stroke="#dcdcdc" stroke-width="1.5"/>

    <rect x="0" y="484" width="759" height="5" fill="var(--red)"/>
    <rect x="0" y="489" width="759" height="49" fill="var(--blue)"/>

    <use href="#burst" x="478" y="293" width="228" height="228" fill="var(--red)" filter="url(#soft)"/>
  </svg>

  <div class="abs brand brand--front">Harlow<br>Contracting</div>
  <div class="abs trades trades--front">Plumbing • Electrical • Hot Water</div>

  <div class="abs address">
    <div class="address__row"><span>Name:</span><i></i></div>
    <div class="address__row"><i></i></div>
    <div class="address__row address__row--gap"><span>Address:</span><i></i></div>
    <div class="address__row"><i></i></div>
    <div class="address__row"><i></i></div>
  </div>

  <div class="abs offer offer--front">
    <div class="offer__amount">$35<span class="offer__off">OFF</span></div>
    <div class="offer__line">Feel The Love With<br>your Next Job</div>
  </div>

  <div class="abs url">www.harlowcontracting.com.au</div>
</section>

<!-- BACK -->
<section class="card card--back">
  <svg class="card__art" viewBox="0 0 759 539">
    <path role="img" aria-label="Photo: glowing blue light bulb" d="M0,0 L400,0 C350,110 328,250 322,366 C220,378 90,420 0,482 Z" fill="url(#glow)"/>
    <path d="M412,0 C362,112 340,252 334,370" fill="none" stroke="var(--red)" stroke-width="9"/>
    <path d="M428,0 C378,114 356,254 350,374" fill="none" stroke="var(--blue)" stroke-width="5"/>
    <path d="M0,490 C110,430 230,392 334,372" fill="none" stroke="var(--red)" stroke-width="8"/>
    <path d="M0,500 C110,442 230,404 340,384" fill="none" stroke="var(--blue)" stroke-width="5"/>

    <rect x="228" y="392" width="507" height="43" rx="3" fill="var(--red)"/>

    <g fill="var(--white)" stroke="var(--red)" stroke-width="2">
      <circle cx="413" cy="285" r="24"/>
      <circle cx="540" cy="285" r="24"/>
      <circle cx="682" cy="285" r="24"/>
    </g>
    <g fill="none" stroke="var(--blue)" stroke-width="2.2" stroke-linecap="round" stroke-linejoin="round">
      <path d="M402,297 V281 H424 V297 M408,281 V275 H418 V281 M398,297 H406 M420,297 H428"/>
      <path d="M534,271 C528,280 534,290 535,298 H545 C546,290 552,280 546,271 M537,301 H543 M537,276 L540,286 L543,276"/>
      <path d="M672,280 H688 C693,280 694,285 694,290 M680,280 V273 M675,273 H685 M694,293 V295 M672,286 H686 C688,286 688,288 688,290"/>
    </g>

    <use href="#burst" x="20" y="306" width="210" height="210" fill="var(--white)" filter="url(#soft)"/>

    <g fill="var(--ink)">
      <path d="M262,456 C267,451 279,451 284,456 L282,460 L278,459 L277,456 H269 L268,459 L264,460 Z"/>
      <rect x="265" y="461" width="16" height="10" rx="2"/>
      <rect x="508" y="456" width="13" height="6" fill="none" stroke="var(--ink)" stroke-width="2"/>
      <rect x="504" y="462" width="21" height="10" rx="2"/>
    </g>

    <rect x="0" y="485" width="759" height="6" fill="var(--red)"/>
    <rect x="0" y="491" width="759" height="48" fill="var(--blue)"/>
  </svg>

  <div class="abs brand brand--back">Harlow<br>Contracting</div>
  <div class="abs trades trades--back">Plumbing • Electrical • Hot Water</div>

  <div class="abs headline headline__top">CALL 1 NUMBER FOR THE</div>
  <div class="abs headline headline__sub">Best In 3 Trades</div>

  <div class="abs service" style="left:355px">Plumbing</div>
  <div class="abs service" style="left:480px">Electrical</div>
  <div class="abs service" style="left:622px">Hot Water</div>

  <div class="abs emergency">
    <span class="emergency__ask">DO YOU HAVE AN EMERGENCY?</span>
    <span class="emergency__num">1800 40 55 21</span>
  </div>

  <div class="abs contact" style="left:292px">Ph: 01 9320 61 48</div>
  <div class="abs contact" style="left:539px">Fax: 9320 7716</div>

  <div class="abs offer offer--back">
    <div class="offer__amount">$XX<span class="offer__off">OFF</span></div>
  </div>

  <div class="abs url">www.harlowcontracting.com.au</div>
</section>

</body>
</html>
```